Pebble Ledger WEB application

We need a small webdesign for a WEB-Application. Functionality will be provided by our developers. All we need are templates with HTML5, CSS and Java functionality for the "animated" parts. As well as some images and logos .
See attached Powerpoint. Please ignore last slide.
Design should be state of the art material design as know from Quorvix or Zelpad latest OS versions
In the end will be fluid design (fitting automatically to actual screen size) but template should base on 540 x 960

Target Market(s)

UK Mobile Market

Number of Pages Required

5+ page

Font styles to use
Sans Serif

Requirements
Must have
• next to requierements in Powerpoint we need animations as stated in PP (progress animation).
Nice to have
• All textfiles should be in a XML file to be easily translated to other languages.Can be done by our developers as well

```html
<!DOCTYPE html>
<html lang="en">
<head>
<meta charset="utf-8">
<title>Pebble Ledger – Battery Optimization</title>
<link rel="stylesheet" href="https://fonts.googleapis.com/css2?family=Raleway:wght@400;600;700;800&display=swap">
<style>
  :root{
    --blue:#1e88e5;
    --blue-dark:#1565c0;
    --ink:#222831;
    --text:#444b52;
    --muted:#6b7278;
    --track:#e6e8ea;
    --panel:#f4f5f6;
    --band:#000;
    --battery:#263238;
    --white:#fff;
  }
  *{box-sizing:border-box;margin:0;padding:0}
  html,body{width:742px;height:1200px;overflow:hidden;background:var(--band)}
  body{font-family:"Raleway",Arial,sans-serif;position:relative;font-variant-numeric:lining-nums;font-feature-settings:"lnum" 1}
  .status-bar{position:absolute;left:0;top:0;width:742px;height:59px;background:var(--blue);color:var(--white)}
  .status-bar .loader{position:absolute;left:18px;top:10px}
  .status-bar .icons{position:absolute;right:118px;top:15px}
  .status-bar .clock{position:absolute;right:22px;top:16px;font-size:24px;font-weight:600;letter-spacing:1px;white-space:nowrap}
  .screen{position:absolute;left:50px;top:59px;width:642px;height:1066px;background:var(--panel)}
  .title{position:absolute;left:0;right:0;top:50px;text-align:center;font-size:37px;font-weight:800;line-height:48px;color:var(--ink);letter-spacing:.5px}
  .gauge{position:absolute;left:210px;top:164px}
  .life-time{position:absolute;left:0;right:0;top:443px;text-align:center;font-size:27px;font-weight:800;color:var(--ink);white-space:nowrap}
  .stats{position:absolute;left:36px;top:536px;width:600px;list-style:none}
  .stat{position:relative;height:56px;display:flex;align-items:center;white-space:nowrap}
  .stat svg{width:30px;height:30px;flex:none}
  .stat-label{flex:none;width:153px;margin-left:20px;font-size:18px;font-weight:600;color:var(--text)}
  .stat-track{flex:none;width:304px;height:8px;background:var(--track);position:relative}
  .stat-fill{position:absolute;left:0;top:0;height:8px;background:var(--blue)}
  .stat-value{flex:none;margin-left:20px;font-size:17px;font-weight:600;color:var(--muted);white-space:nowrap}
  .cta{position:absolute;left:98px;top:950px;width:453px;height:74px;background:var(--blue);color:var(--white);white-space:nowrap;
       display:flex;align-items:center;justify-content:center;font-size:25px;font-weight:800;letter-spacing:.3px}
  .footer{position:absolute;left:0;top:1125px;width:742px;height:75px;background:var(--blue);color:var(--white);text-align:center}
  .social{padding-top:12px;font-size:15px;font-weight:700;letter-spacing:1px}
  .social span{margin:0 6px}
  .copyright{margin-top:8px;font-size:16px;font-weight:400}
</style>
</head>
<body>
<header class="status-bar">
  <svg class="loader" width="40" height="40" viewBox="0 0 40 40" aria-hidden="true">
    <circle cx="20" cy="20" r="16" fill="none" stroke="#fff" stroke-width="3" stroke-dasharray="5 4"/>
    <text x="20" y="25" text-anchor="middle" font-size="13" font-family="Raleway, sans-serif" font-weight="700" fill="#fff">40</text>
  </svg>
  <svg class="icons" width="110" height="30" viewBox="0 0 110 30" aria-hidden="true">
    <circle cx="14" cy="16" r="10" fill="none" stroke="#fff" stroke-width="3"/>
    <path d="M14 10v6l4 3" stroke="#fff" stroke-width="2.5" fill="none"/>
    <path d="M4 5l5-3M24 5l-5-3" stroke="#fff" stroke-width="2.5"/>
    <path d="M42 12a20 20 0 0 1 28 0M46 17a13 13 0 0 1 20 0M51 22a6 6 0 0 1 10 0" stroke="#fff" stroke-width="3" fill="none"/>
    <rect x="88" y="5" width="12" height="22" rx="1.5" fill="#fff"/>
    <rect x="91" y="2" width="6" height="4" fill="#fff"/>
  </svg>
  <div class="clock">21 : 30</div>
</header>

<main class="screen">
  <h1 class="title">OVER ALL BATTERY<br>OPTIMIZATION</h1>

  <svg class="gauge" width="222" height="222" viewBox="0 0 222 222" aria-label="Battery at 26 percent">
    <defs><clipPath id="gauge-clip"><circle cx="111" cy="111" r="111"/></clipPath></defs>
    <circle cx="111" cy="111" r="111" fill="var(--blue)"/>
    <polygon points="82,60 140,60 262,182 262,262 200,262 82,160" fill="var(--blue-dark)" clip-path="url(#gauge-clip)"/>
    <rect x="99" y="46" width="24" height="10" fill="var(--battery)"/>
    <rect x="82" y="56" width="58" height="108" fill="var(--battery)"/>
    <text x="111" y="118" text-anchor="middle" font-family="Raleway, sans-serif" font-weight="700" font-size="22" fill="var(--blue)" style="font-feature-settings:'lnum' 1">26%</text>
  </svg>

  <p class="life-time">INCREASE BATTERY LIFE TIME: 3H50MIN</p>

  <ul class="stats">
    <li class="stat">
      <svg viewBox="0 0 30 30" aria-hidden="true"><circle cx="15" cy="15" r="11" fill="var(--blue)"/></svg>
      <span class="stat-label">System</span>
      <span class="stat-track"><span class="stat-fill" style="width:274px"></span></span>
      <span class="stat-value">90 %</span>
    </li>
    <li class="stat">
      <svg viewBox="0 0 30 30" aria-hidden="true"><rect x="5" y="5" width="20" height="20" rx="4" fill="var(--blue)"/><rect x="10" y="10" width="10" height="10" fill="#fff"/></svg>
      <span class="stat-label">Memory</span>
      <span class="stat-track"><span class="stat-fill" style="width:152px"></span></span>
      <span class="stat-value">50 %</span>
    </li>
    <li class="stat">
      <svg viewBox="0 0 30 30" aria-hidden="true"><circle cx="9" cy="20" r="5" fill="none" stroke="var(--blue)" stroke-width="3"/><path d="M13 16l12-11M20 10l3 3M23 7l3 3" stroke="var(--blue)" stroke-width="3"/></svg>
      <span class="stat-label">Accounts</span>
      <span class="stat-track"><span class="stat-fill" style="width:97px"></span></span>
      <span class="stat-value">32 %</span>
    </li>
    <li class="stat">
      <svg viewBox="0 0 30 30" aria-hidden="true"><path d="M6 15a9 9 0 0 1 15-7M24 15a9 9 0 0 1-15 7" fill="none" stroke="var(--blue)" stroke-width="3"/><path d="M18 4l5 4-5 3zM12 26l-5-4 5-3z" fill="var(--blue)"/></svg>
      <span class="stat-label">Sync Processes</span>
      <span class="stat-track"><span class="stat-fill" style="width:204px"></span></span>
      <span class="stat-value">67 %</span>
    </li>
    <li class="stat">
      <svg viewBox="0 0 30 30" aria-hidden="true"><path d="M15 3a8 8 0 0 1 8 8c0 6-8 16-8 16S7 17 7 11a8 8 0 0 1 8-8z" fill="var(--blue)"/><circle cx="15" cy="11" r="3" fill="#fff"/></svg>
      <span class="stat-label">Localization</span>
      <span class="stat-track"><span class="stat-fill" style="width:112px"></span></span>
      <span class="stat-value">37 %</span>
    </li>
    <li class="stat">
      <svg viewBox="0 0 30 30" aria-hidden="true"><circle cx="15" cy="15" r="11" fill="var(--blue)"/></svg>
      <span class="stat-label">Bluetooth</span>
      <span class="stat-track"><span class="stat-fill" style="width:52px"></span></span>
      <span class="stat-value">17 %</span>
    </li>
    <li class="stat">
      <svg viewBox="0 0 30 30" aria-hidden="true"><circle cx="15" cy="15" r="11" fill="none" stroke="var(--blue)" stroke-width="2.5"/><ellipse cx="15" cy="15" rx="5" ry="11" fill="none" stroke="var(--blue)" stroke-width="2"/><path d="M4 15h22M6 9h18M6 21h18" stroke="var(--blue)" stroke-width="2"/></svg>
      <span class="stat-label">Apps</span>
      <span class="stat-track"><span class="stat-fill" style="width:283px"></span></span>
      <span class="stat-value">93 %</span>
    </li>
  </ul>

  <div class="cta">START FREE OPTIMIZATION NOW</div>
</main>

<footer class="footer">
  <div class="social"><span>Nivo</span><span>Tapr</span><span>Qrin</span><span>Wisp</span></div>
  <p class="copyright">Copyright © 2015 . All rights reserved.</p>
</footer>
</body>
</html>
```